Dean harlow realestate

We want something complete different to our website now and something that will stand out this is our website http://deanharlowrealestate-example.com/

our company website for my boss is www.trevorvance-example.com

please note this website is being made for dean harlow not trevor vance

something similar to our company website but has to be in the branding of dean harlow realestate

```html
<!DOCTYPE html>
<html lang="en">
<head>
<meta charset="utf-8">
<title>Dean Harlow Property</title>
<link href="https://fonts.googleapis.com/css2?family=Open+Sans:ital,wght@0,400;0,600;0,700;0,800;1,400&display=swap" rel="stylesheet">
<style>
:root{
  --gold:#b8936a;
  --navy:#27315a;
  --ink:#1f2133;
  --body:#555;
  --line:#d8d8d8;
  --white:#fff;
}
*{box-sizing:border-box;margin:0;padding:0}
html,body{width:1200px;height:3529px;overflow:hidden}
body{font-family:"Open Sans",Arial,sans-serif;color:var(--ink);background:var(--white);position:relative}
.hero{position:absolute;left:0;top:0;width:1200px;height:628px;
  background:linear-gradient(180deg,#5a4a3c 0%,#8a6c4c 22%,#6d7f8f 50%,#3a4f66 78%,#25364c 100%);}
.hero-shade{position:absolute;inset:0;background:linear-gradient(180deg,rgba(0,0,0,.35),rgba(0,0,0,.1) 40%,rgba(0,0,0,.25))}
.brand{position:absolute;left:99px;top:38px;display:flex;align-items:center;gap:16px;color:var(--white);font-weight:700}
.brand-dot{width:70px;height:70px;border-radius:50%;background:var(--white)}
.brand-name{font-size:30px;line-height:34px;letter-spacing:.5px}
.brand-name span{display:block;font-size:17px;letter-spacing:5px;text-align:center}
.topbar{position:absolute;right:96px;top:28px;color:var(--white);font-size:16px;display:flex;gap:12px;align-items:center}
.topbar svg{fill:var(--gold);vertical-align:-2px;margin-right:6px}
.nav{position:absolute;right:96px;top:72px;display:flex;gap:34px;align-items:center;font-size:16px;font-weight:600;color:var(--white)}
.nav .active{color:var(--gold)}
.hero-title{position:absolute;top:218px;width:100%;text-align:center;color:var(--white);font-size:66px;font-weight:800;letter-spacing:1px}
.hero-sub{position:absolute;top:300px;width:100%;text-align:center;color:var(--white);font-size:27px;font-weight:600}
.hero-btn{position:absolute;left:474px;top:368px;width:252px;height:54px;border:2px solid var(--white);border-radius:27px;color:var(--white);font-size:16px;font-weight:700;display:flex;align-items:center;justify-content:center}
.section-title{position:absolute;top:705px;width:100%;text-align:center;font-size:38px;font-weight:700;color:var(--ink)}
.pill{position:absolute;top:788px;height:50px;border:2px solid var(--gold);border-radius:25px;color:var(--gold);font-size:15px;font-weight:600;display:flex;align-items:center;justify-content:center}
.listing{position:absolute;left:99px;width:1004px;height:326px;border-bottom:2px solid var(--line)}
.listing-photo{position:absolute;left:0;top:0;width:330px;height:250px;border:3px solid #e2e2e2}
.listing-price{position:absolute;left:386px;top:-2px;font-size:21px;color:var(--ink)}
.listing-price b{color:var(--navy);font-weight:700}
.listing-address{position:absolute;left:386px;top:36px;font-size:23px;font-weight:700;color:var(--navy)}
.listing-suburb{position:absolute;left:386px;top:80px;font-size:16px;color:var(--ink)}
.listing-suburb svg{fill:var(--navy);vertical-align:-2px;margin-right:6px}
.listing-desc{position:absolute;left:386px;top:116px;width:610px;font-size:15.5px;line-height:27px;color:var(--body)}
.listing-feats{position:absolute;left:386px;top:218px;display:flex;gap:36px;font-size:15px;color:var(--body)}
.listing-feats span{display:flex;align-items:center;gap:12px}
.listing-feats svg{fill:var(--gold)}
.more-btn{position:absolute;left:508px;top:2560px;width:184px;height:58px;border-radius:29px;background:var(--gold);color:var(--white);font-size:17px;font-weight:700;display:flex;align-items:center;justify-content:center}
.reviews{position:absolute;left:0;top:2705px;width:1200px;height:330px;background:var(--navy)}
.reviews h2{position:absolute;top:60px;width:100%;text-align:center;color:var(--white);font-size:33px;font-weight:700}
.reviews blockquote{position:absolute;left:225px;top:126px;width:750px;text-align:center;color:var(--white);font-size:17px;line-height:31px;font-style:italic}
.reviews cite{position:absolute;top:228px;width:100%;text-align:center;color:var(--white);font-size:18px;font-style:normal;font-weight:700}
.reviews cite small{font-weight:400;font-size:15px}
.arrow-btn{position:absolute;top:142px;width:48px;height:48px;border-radius:50%;background:rgba(255,255,255,.18);display:flex;align-items:center;justify-content:center}
.arrow-btn svg{stroke:var(--white);fill:none;stroke-width:2.5}
.block-title{position:absolute;top:3118px;font-size:19px;font-weight:700;color:var(--ink)}
.field{position:absolute;height:32px;border:1.5px solid #b9b9b9;font-size:12px;color:#666;padding:7px 12px}
.submit{position:absolute;left:631px;top:3374px;width:96px;height:36px;border-radius:18px;background:var(--gold);color:var(--white);font-size:14px;font-weight:700;display:flex;align-items:center;justify-content:center}
.info{position:absolute;left:781px;display:flex;align-items:center;gap:22px;font-size:14px;line-height:23px;color:#444}
.info i{width:36px;height:36px;border:1.5px solid #bbb;border-radius:50%;display:flex;align-items:center;justify-content:center;flex:none}
.info svg{fill:var(--navy)}
.social{position:absolute;left:781px;top:3374px;display:flex;gap:10px}
.social span{width:33px;height:33px;border-radius:50%;background:var(--navy)}
.footer-rule{position:absolute;left:99px;top:3440px;width:1004px;border-top:1.5px solid var(--line)}
.copyright{position:absolute;top:3468px;width:100%;text-align:center;font-size:14px;color:#444}
.to-top{position:absolute;left:1072px;top:3468px}
</style>
</head>
<body>

<header class="hero">
  <div class="hero-shade" role="img" aria-label="City skyline of glass towers at sunset"></div>
  <div class="brand"><div class="brand-dot"></div><div class="brand-name">DEAN HARLOW<span>PROPERTY</span></div></div>
  <div class="topbar">
    <span><svg width="14" height="14" viewBox="0 0 24 24"><path d="M6.6 10.8a15.1 15.1 0 0 0 6.6 6.6l2.2-2.2a1 1 0 0 1 1-.25 11.4 11.4 0 0 0 3.6.57 1 1 0 0 1 1 1V20a1 1 0 0 1-1 1A17 17 0 0 1 3 4a1 1 0 0 1 1-1h3.5a1 1 0 0 1 1 1c0 1.25.2 2.45.57 3.57a1 1 0 0 1-.25 1z"/></svg>0412 555 318</span>
    <span>|</span>
    <span><svg width="15" height="13" viewBox="0 0 24 20"><path d="M2 0h20a2 2 0 0 1 2 2v1L12 10 0 3V2a2 2 0 0 1 2-2zm-2 5.3 12 7 12-7V18a2 2 0 0 1-2 2H2a2 2 0 0 1-2-2z"/></svg>dean@trevorvance-example.com</span>
  </div>
  <nav class="nav">
    <span class="active">HOME</span><span>FOR SALE</span><span>AGENTS</span><span>BOOK APPRAISAL</span><span>CONTACT</span>
    <svg width="16" height="16" viewBox="0 0 24 24" fill="none" stroke="#fff" stroke-width="3"><circle cx="10" cy="10" r="7"/><path d="M15 15l7 7"/></svg>
  </nav>
  <h1 class="hero-title">DEAN HARLOW PROPERTY</h1>
  <p class="hero-sub">Nemo enim ipsam voluptatem quia voluptas sit aspernatur aut</p>
  <div class="hero-btn">UPCOMING HOME OPENS</div>
</header>

<h2 class="section-title">LATEST PROPERTIES FOR SALE</h2>
<div class="pill" style="left:337px;width:254px">RECEIVE PROPERTY ALERTS</div>
<div class="pill" style="left:608px;width:256px">VIEW PROJECT PLANS</div>

<article class="listing" style="top:913px">
  <div class="listing-photo" role="img" aria-label="Grey single-storey home with garage under a cloudy sky" style="background:linear-gradient(180deg,#7fa7d6 0%,#c9d6e3 40%,#9aa0a6 65%,#b9b5ad 100%)"></div>
  <p class="listing-price">FROM <b>$549,000 - $589,000</b></p>
  <h3 class="listing-address">14 LARKSPUR LANE, RIVERVALE, WA 6103</h3>
  <p class="listing-suburb"><svg width="10" height="14" viewBox="0 0 10 14"><path d="M5 0a5 5 0 0 1 5 5c0 3.5-5 9-5 9S0 8.5 0 5a5 5 0 0 1 5-5zm0 3a2 2 0 1 0 0 4 2 2 0 0 0 0-4z"/></svg>Belmont</p>
  <p class="listing-desc">Light, bright and airy, the open plan living/dining/kitchen zone has a beautiful flow out to the alfresco entertaining areas. Situated on a 293sqm block makes this property low maintenance. Easy access to Wattle Park, Heron Park, Reed Lake..</p>
  <div class="listing-feats"><span><svg width="22" height="14" viewBox="0 0 22 14"><path d="M0 0h3v7h19v7h-3v-3H3v3H0zM4 3h6v3H4zm7 0h9a2 2 0 0 1 2 2v1H11z"/></svg>3</span><span><svg width="20" height="16" viewBox="0 0 20 16"><path d="M0 6h20v3a5 5 0 0 1-5 5H5a5 5 0 0 1-5-5zM3 14l-1 2h2l1-2zm12 0 1 2h2l-1-2zM14 0h3v6h-3z"/></svg>2</span><span><svg width="20" height="18" viewBox="0 0 20 18"><path d="M0 0h10v4H4v4h6v4H0zm8 9h12v6H8zm2 7h2v2h-2zm6 0h2v2h-2z"/></svg>2</span></div>
</article>

<article class="listing" style="top:1238px">
  <div class="listing-photo" role="img" aria-label="Two-storey red brick home with white garage door" style="background:linear-gradient(180deg,#4e8ad0 0%,#9fc0e6 25%,#a45a44 50%,#8c4a38 75%,#cfcfcf 100%)"></div>
  <p class="listing-price">FROM <b>$549,000 - $589,000</b></p>
  <h3 class="listing-address">14 LARKSPUR LANE, RIVERVALE, WA 6103</h3>
  <p class="listing-suburb"><svg width="10" height="14" viewBox="0 0 10 14"><path d="M5 0a5 5 0 0 1 5 5c0 3.5-5 9-5 9S0 8.5 0 5a5 5 0 0 1 5-5zm0 3a2 2 0 1 0 0 4 2 2 0 0 0 0-4z"/></svg>Belmont</p>
  <p class="listing-desc">Light, bright and airy, the open plan living/dining/kitchen zone has a beautiful flow out to the alfresco entertaining areas. Situated on a 293sqm block makes this property low maintenance. Easy access to Wattle Park, Heron Park, Reed Lake..</p>
  <div class="listing-feats"><span><svg width="22" height="14" viewBox="0 0 22 14"><path d="M0 0h3v7h19v7h-3v-3H3v3H0zM4 3h6v3H4zm7 0h9a2 2 0 0 1 2 2v1H11z"/></svg>3</span><span><svg width="20" height="16" viewBox="0 0 20 16"><path d="M0 6h20v3a5 5 0 0 1-5 5H5a5 5 0 0 1-5-5zM3 14l-1 2h2l1-2zm12 0 1 2h2l-1-2zM14 0h3v6h-3z"/></svg>2</span><span><svg width="20" height="18" viewBox="0 0 20 18"><path d="M0 0h10v4H4v4h6v4H0zm8 9h12v6H8zm2 7h2v2h-2zm6 0h2v2h-2z"/></svg>2</span></div>
</article>

<article class="listing" style="top:1563px">
  <div class="listing-photo" role="img" aria-label="Modern home with gated entry at dusk" style="background:linear-gradient(180deg,#3d4f7a 0%,#8a7fa0 25%,#3d3a38 55%,#6a4c38 80%,#a4503a 100%)"></div>
  <p class="listing-price">FROM <b>$549,000 - $589,000</b></p>
  <h3 class="listing-address">14 LARKSPUR LANE, RIVERVALE, WA 6103</h3>
  <p class="listing-suburb"><svg width="10" height="14" viewBox="0 0 10 14"><path d="M5 0a5 5 0 0 1 5 5c0 3.5-5 9-5 9S0 8.5 0 5a5 5 0 0 1 5-5zm0 3a2 2 0 1 0 0 4 2 2 0 0 0 0-4z"/></svg>Belmont</p>
  <p class="listing-desc">Light, bright and airy, the open plan living/dining/kitchen zone has a beautiful flow out to the alfresco entertaining areas. Situated on a 293sqm block makes this property low maintenance. Easy access to Wattle Park, Heron Park, Reed Lake..</p>
  <div class="listing-feats"><span><svg width="22" height="14" viewBox="0 0 22 14"><path d="M0 0h3v7h19v7h-3v-3H3v3H0zM4 3h6v3H4zm7 0h9a2 2 0 0 1 2 2v1H11z"/></svg>3</span><span><svg width="20" height="16" viewBox="0 0 20 16"><path d="M0 6h20v3a5 5 0 0 1-5 5H5a5 5 0 0 1-5-5zM3 14l-1 2h2l1-2zm12 0 1 2h2l-1-2zM14 0h3v6h-3z"/></svg>2</span><span><svg width="20" height="18" viewBox="0 0 20 18"><path d="M0 0h10v4H4v4h6v4H0zm8 9h12v6H8zm2 7h2v2h-2zm6 0h2v2h-2z"/></svg>2</span></div>
</article>

<article class="listing" style="top:1888px">
  <div class="listing-photo" role="img" aria-label="Tan brick home with garage and paved driveway" style="background:linear-gradient(180deg,#3f7fd0 0%,#8fb6e2 30%,#b48c62 55%,#a07c58 75%,#b7866a 100%)"></div>
  <p class="listing-price">FROM <b>$549,000 - $589,000</b></p>
  <h3 class="listing-address">14 LARKSPUR LANE, RIVERVALE, WA 6103</h3>
  <p class="listing-suburb"><svg width="10" height="14" viewBox="0 0 10 14"><path d="M5 0a5 5 0 0 1 5 5c0 3.5-5 9-5 9S0 8.5 0 5a5 5 0 0 1 5-5zm0 3a2 2 0 1 0 0 4 2 2 0 0 0 0-4z"/></svg>Belmont</p>
  <p class="listing-desc">Light, bright and airy, the open plan living/dining/kitchen zone has a beautiful flow out to the alfresco entertaining areas. Situated on a 293sqm block makes this property low maintenance. Easy access to Wattle Park, Heron Park, Reed Lake..</p>
  <div class="listing-feats"><span><svg width="22" height="14" viewBox="0 0 22 14"><path d="M0 0h3v7h19v7h-3v-3H3v3H0zM4 3h6v3H4zm7 0h9a2 2 0 0 1 2 2v1H11z"/></svg>3</span><span><svg width="20" height="16" viewBox="0 0 20 16"><path d="M0 6h20v3a5 5 0 0 1-5 5H5a5 5 0 0 1-5-5zM3 14l-1 2h2l1-2zm12 0 1 2h2l-1-2zM14 0h3v6h-3z"/></svg>2</span><span><svg width="20" height="18" viewBox="0 0 20 18"><path d="M0 0h10v4H4v4h6v4H0zm8 9h12v6H8zm2 7h2v2h-2zm6 0h2v2h-2z"/></svg>2</span></div>
</article>

<article class="listing" style="top:2213px">
  <div class="listing-photo" role="img" aria-label="White two-storey home with wide garage door" style="background:linear-gradient(180deg,#6f9ad4 0%,#c9d5e2 30%,#e6e6e6 55%,#b9bcc0 80%,#8e9094 100%)"></div>
  <p class="listing-price">FROM <b>$549,000 - $589,000</b></p>
  <h3 class="listing-address">14 LARKSPUR LANE, RIVERVALE, WA 6103</h3>
  <p class="listing-suburb"><svg width="10" height="14" viewBox="0 0 10 14"><path d="M5 0a5 5 0 0 1 5 5c0 3.5-5 9-5 9S0 8.5 0 5a5 5 0 0 1 5-5zm0 3a2 2 0 1 0 0 4 2 2 0 0 0 0-4z"/></svg>Belmont</p>
  <p class="listing-desc">Light, bright and airy, the open plan living/dining/kitchen zone has a beautiful flow out to the alfresco entertaining areas. Situated on a 293sqm block makes this property low maintenance. Easy access to Wattle Park, Heron Park, Reed Lake..</p>
  <div class="listing-feats"><span><svg width="22" height="14" viewBox="0 0 22 14"><path d="M0 0h3v7h19v7h-3v-3H3v3H0zM4 3h6v3H4zm7 0h9a2 2 0 0 1 2 2v1H11z"/></svg>3</span><span><svg width="20" height="16" viewBox="0 0 20 16"><path d="M0 6h20v3a5 5 0 0 1-5 5H5a5 5 0 0 1-5-5zM3 14l-1 2h2l1-2zm12 0 1 2h2l-1-2zM14 0h3v6h-3z"/></svg>2</span><span><svg width="20" height="18" viewBox="0 0 20 18"><path d="M0 0h10v4H4v4h6v4H0zm8 9h12v6H8zm2 7h2v2h-2zm6 0h2v2h-2z"/></svg>2</span></div>
</article>

<div class="more-btn">VIEW MORE</div>

<section class="reviews">
  <h2>WHAT OUR CLIENTS THINK</h2>
  <div class="arrow-btn" style="left:99px"><svg width="12" height="18" viewBox="0 0 12 18"><path d="M9 2 3 9l6 7"/></svg></div>
  <div class="arrow-btn" style="left:1053px"><svg width="12" height="18" viewBox="0 0 12 18"><path d="M3 2l6 7-6 7"/></svg></div>
  <blockquote>" We bought our first home through Dean and the process was easy and very straight forward. We felt confident buying our first home and extremely supported. We put a few offers forward on other properties with other local agents but we didn't feel that piece of mind that we felt with Dean. "</blockquote>
  <cite>- Marisa &amp; Tomas <small>Kewdale, 6105</small></cite>
</section>

<h3 class="block-title" style="left:97px">CONTACT FORM</h3>
<div class="field" style="left:99px;top:3180px;width:311px">Name :</div>
<div class="field" style="left:419px;top:3180px;width:308px">Phone no :</div>
<div class="field" style="left:99px;top:3226px;width:628px">Email :</div>
<div class="field" style="left:99px;top:3272px;width:628px;height:82px">Message :</div>
<div class="submit">SUBMIT</div>

<h3 class="block-title" style="left:781px">CONTACT INFORMATION</h3>
<div class="info" style="top:3166px"><i><svg width="10" height="14" viewBox="0 0 10 14"><path d="M5 0a5 5 0 0 1 5 5c0 3.5-5 9-5 9S0 8.5 0 5a5 5 0 0 1 5-5zm0 3a2 2 0 1 0 0 4 2 2 0 0 0 0-4z"/></svg></i><span>Suite 12, 8 Ashgrove Road,<br>Rivervale, WA 6103 Australia</span></div>
<div class="info" style="top:3223px"><i><svg width="13" height="13" viewBox="0 0 24 24"><path d="M6.6 10.8a15.1 15.1 0 0 0 6.6 6.6l2.2-2.2a1 1 0 0 1 1-.25 11.4 11.4 0 0 0 3.6.57 1 1 0 0 1 1 1V20a1 1 0 0 1-1 1A17 17 0 0 1 3 4a1 1 0 0 1 1-1h3.5a1 1 0 0 1 1 1c0 1.25.2 2.45.57 3.57a1 1 0 0 1-.25 1z"/></svg></i><span>0412 555 318</span></div>
<div class="info" style="top:3274px"><i><svg width="14" height="12" viewBox="0 0 24 20"><path d="M2 0h20a2 2 0 0 1 2 2v1L12 10 0 3V2a2 2 0 0 1 2-2zm-2 5.3 12 7 12-7V18a2 2 0 0 1-2 2H2a2 2 0 0 1-2-2z"/></svg></i><span>dean@trevorvance-example.com</span></div>
<h3 class="block-title" style="left:781px;top:3328px">SOCIAL MEDIA</h3>
<div class="social" aria-label="Social media links"><span></span><span></span><span></span><span></span></div>

<div class="footer-rule"></div>
<p class="copyright">Copyright © 2018, Dean Harlow Property . All rights reserved.</p>
<svg class="to-top" width="30" height="18" viewBox="0 0 30 18" fill="none" stroke="#aaa" stroke-width="3"><path d="M3 15 15 4l12 11"/></svg>

</body>
</html>
```